TrakVora Presentation of its Lanebright Product

Our company creates real time tracking solutions that solve problems with location.

Our flagship product is and application that allows parents and students to know the real time location of the school bus. The application is integrated with a Fleet Management back end that helps School Transportation directors manage the School Bus fleet.

See our website at www.trakvora-example.com

The purpose of this contest is to design a PowerPoint to present our Lanebright Product to School District clients. The presentation must cover the following features:

Lanebright Demonstration
* History Lookup
* Update Route
* Fleet View
* Manage Bus Stops
* Miles Driven Report
* Manage Routes (Print Route Instructions)
* Find My Routes
* Substitute a Bus
* Mobile Web App
Key Differentiators
Implementation
Pricing

I have attached a PPT to be used as an outline of the presentation. Each slide in the outline contains a link or otherwise provides reference material that will help you understand the feature.

I have attached images related to each feature that may be used to help tell the story.

In the slide master you must include page numbers beginning with page 2 (no page number on the cover sheet, in the footer include the words "TrakVora, LLC CONFIDENTIAL AND PROPRIETARY", also include the TrakVora log which you will find attached.

I have attached a creative brief and branding document. The winning design will have read these documents and woven the verbiage and ideas in these documents into the presentation.

TrakVora logo color codes are:
green: #89af2e
blue: #006fba

Please use your creative freedom to design something great!

Target Market(s)

American School Districts (Kindergarten through 12th grade), specifically, School Transportation Directors and Superintendents.

Industry/Entity Type

It Company

Requirements
Must have
• The TrakVora Logo in the Slide Master. Language from the attached branding document and creative brief woven through the presentation.
Nice to have
• It will be important to have designs associated with each page type so that we may use a clean copy of this design for all our presentations.
• Consider the logo when selecting the fonts.

```html
<!DOCTYPE html>
<html lang="en">
<head>
<meta charset="utf-8">
<title>TrakVora – Lanebright Presentation Slides</title>
<link rel="stylesheet" href="https://fonts.googleapis.com/css2?family=Arimo:ital,wght@0,400;0,700;1,400&family=Questrial&family=Tinos:ital@1&display=swap">
<style>
  :root{
    --stage:#707070;
    --white:#ffffff;
    --blue:#006fba;
    --blue-mid:#1a73c0;
    --green:#89af2e;
    --green-lite:#8dc63f;
    --orange:#e8892a;
    --purple:#7030a0;
    --brown:#8b6a4a;
    --cyan:#1aa3e0;
    --rose:#9b4d4d;
    --slate:#5b7593;
    --ink:#222222;
    --grey:#777777;
    --line:#9a9a9a;
    --art-grey:#c4c4c4;
  }
  html,body{margin:0;padding:0;}
  body{width:1200px;height:799px;overflow:hidden;background:var(--stage);position:relative;}
  .slide{position:absolute;background:var(--white);overflow:hidden;}
  .slide svg{display:block;width:100%;height:100%;}
  .slide--cover{left:75px;top:40px;width:449px;height:320px;}
  .slide--demo{left:77px;top:430px;width:450px;height:329px;}
  .slide--differentiators{left:637px;top:102px;width:238px;height:179px;}
  .slide--implementation-a{left:890px;top:95px;width:237px;height:181px;}
  .slide--implementation-b{left:638px;top:330px;width:234px;height:172px;}
  .slide--pricing-a{left:883px;top:330px;width:255px;height:173px;}
  .slide--pricing-b{left:780px;top:559px;width:256px;height:181px;}

  .t-title{font-family:"Questrial",sans-serif;fill:var(--white);}
  .t-head{font-family:"Arimo",sans-serif;font-weight:700;}
  .t-body{font-family:"Arimo",sans-serif;fill:var(--ink);}
  .t-muted{font-family:"Arimo",sans-serif;fill:var(--grey);}
  .t-brand{font-family:"Arimo",sans-serif;font-weight:700;fill:var(--blue);}
  .t-foot{font-family:"Tinos",serif;font-style:italic;fill:var(--white);}
  .t-num{font-family:"Arimo",sans-serif;font-weight:700;fill:var(--white);}
  .fill-blue{fill:var(--blue);}
  .fill-green{fill:var(--green);}
  .txt-blue{fill:var(--blue);}
  .txt-green{fill:var(--green);}
  .dots{fill:none;stroke:var(--line);stroke-width:1.3;stroke-dasharray:1.5 2;}
  .node{fill:var(--white);stroke:var(--line);stroke-width:1.2;}
  .art{fill:var(--art-grey);}
</style>
</head>
<body>

<!-- Cover -->
<section class="slide slide--cover">
  <svg viewBox="0 0 449 320" xmlns="http://www.w3.org/2000/svg">
    <defs>
      <linearGradient id="snowScene" x1="0" y1="0" x2="0" y2="1">
        <stop offset="0" stop-color="#5f6a6c"/>
        <stop offset="0.45" stop-color="#d9dee0"/>
        <stop offset="1" stop-color="#b8b0a6"/>
      </linearGradient>
    </defs>
    <rect x="0" y="0" width="449" height="200" fill="url(#snowScene)" role="img" aria-label="Photo: a yellow school bus driving along a snowy forest road"/>
    <circle cx="32" cy="168" r="9" class="fill-green"/>
    <text x="46" y="173" class="t-brand" font-size="15">TrakVora</text>
    <polygon points="0,188 449,196 449,240" class="fill-green"/>
    <polygon points="0,188 449,240 449,320 0,320" class="fill-blue"/>
    <text x="345" y="219" class="t-title" font-size="11">2016 Budget</text>
    <text x="27" y="265" class="t-title" font-size="19">Harlow-Brenton Holding Co.</text>
    <text x="27" y="288" class="t-title" font-size="19">2016 Budget Presentation</text>
  </svg>
</section>

<!-- Lanebright Demonstration -->
<section class="slide slide--demo">
  <svg viewBox="0 0 450 329" xmlns="http://www.w3.org/2000/svg">
    <rect x="0" y="11" width="31" height="22" class="fill-blue"/>
    <rect x="33" y="11" width="7" height="22" class="fill-green"/>
    <text x="54" y="29" class="t-head" font-size="14.5"><tspan class="txt-blue">Lanebright</tspan> <tspan class="txt-green">Demonstration</tspan></text>
    <circle cx="387" cy="18" r="6" class="fill-green"/>
    <text x="396" y="22" class="t-brand" font-size="10">TrakVora</text>

    <path class="dots" d="M123,98 V262 H235 V80 H350 V265"/>

    <g class="t-num" font-size="8" text-anchor="middle">
      <rect x="22" y="94" width="77" height="14" fill="var(--blue-mid)"/><text x="60" y="104">01</text>
      <rect x="22" y="138" width="77" height="14" fill="var(--orange)"/><text x="60" y="148">02</text>
      <rect x="22" y="182" width="77" height="14" fill="var(--purple)"/><text x="60" y="192">03</text>
      <rect x="22" y="227" width="77" height="14" fill="var(--brown)"/><text x="60" y="237">04</text>
      <rect x="247" y="95" width="78" height="14" fill="var(--green-lite)"/><text x="286" y="105">05</text>
      <rect x="247" y="139" width="78" height="14" fill="var(--cyan)"/><text x="286" y="149">06</text>
      <rect x="247" y="183" width="78" height="14" fill="var(--rose)"/><text x="286" y="193">07</text>
      <rect x="247" y="223" width="78" height="14" fill="var(--blue-mid)"/><text x="286" y="233">08</text>
      <rect x="247" y="260" width="78" height="14" fill="var(--slate)"/><text x="286" y="270">09</text>
    </g>

    <g>
      <circle cx="123" cy="98" r="3" fill="var(--line)"/>
      <circle cx="123" cy="145" r="3.2" class="node"/>
      <circle cx="123" cy="192" r="3.2" class="node"/>
      <circle cx="123" cy="238" r="3.2" class="node"/>
      <circle cx="350" cy="102" r="3.2" class="node"/>
      <circle cx="350" cy="145" r="3.2" class="node"/>
      <circle cx="350" cy="191" r="3.2" class="node"/>
      <circle cx="350" cy="229" r="3.2" class="node"/>
      <circle cx="350" cy="267" r="3" fill="var(--line)"/>
    </g>

    <g class="t-body" font-size="7.6">
      <text x="138" y="101">History Lookup</text>
      <text x="138" y="148">Update Route</text>
      <text x="138" y="195">Fleet View</text>
      <text x="136" y="241">Manage Bus Stops</text>
      <text x="364" y="99">Miles Driven</text>
      <text x="364" y="109">Report</text>
      <text x="364" y="139">Manage Routes</text>
      <text x="364" y="148">(Print Route</text>
      <text x="364" y="157">Instructions)</text>
      <text x="364" y="195">Find My Routes</text>
      <text x="364" y="232">Substitute a Bus</text>
      <text x="364" y="267">Mobile Web</text>
      <text x="364" y="277">App</text>
    </g>

    <polygon points="0,310 335,310 341,329 0,329" class="fill-blue"/>
    <polygon points="350,310 450,310 450,329 356,329" class="fill-green"/>
    <text x="11" y="323" class="t-foot" font-size="7">Harlow-Brenton Holding Co: December 11, 2015</text>
    <text x="343" y="324" class="t-body" font-size="9">1</text>
    <text x="364" y="323" class="t-foot" font-size="7">Proprietary &amp; Confidential</text>
  </svg>
</section>

<!-- Key Differentiators -->
<section class="slide slide--differentiators">
  <svg viewBox="0 0 238 179" xmlns="http://www.w3.org/2000/svg">
    <rect x="0" y="6" width="15" height="12" class="fill-blue"/><rect x="17" y="6" width="4" height="12" class="fill-green"/>
    <text x="28" y="16" class="t-head txt-blue" font-size="7.5">Key <tspan class="txt-green">Differentiators</tspan></text>
    <circle cx="203" cy="10" r="3" class="fill-green"/><text x="208" y="12" class="t-brand" font-size="5">TrakVora</text>

    <rect x="73" y="33" width="93" height="128" rx="6" fill="#1b1b1b"/>
    <rect x="80" y="44" width="79" height="106" fill="#8e9294" role="img" aria-label="Photo: a hand touching a tablet screen showing a city skyline"/>

    <g fill="var(--blue-mid)">
      <circle cx="50" cy="64" r="6"/><circle cx="50" cy="104" r="6"/>
      <circle cx="180" cy="64" r="6"/><circle cx="180" cy="104" r="6"/>
    </g>
    <g fill="var(--white)">
      <rect x="47" y="62" width="6" height="4"/><rect x="47" y="102" width="6" height="4"/>
      <rect x="178" y="61" width="4" height="6"/><rect x="177.5" y="101" width="5" height="6"/>
    </g>
    <g class="t-body" font-size="3.2" text-anchor="end">
      <text x="58" y="76" font-weight="700">Title one</text>
      <text x="60" y="81">Live bus location for parents.</text>
      <text x="58" y="116" font-weight="700">Title Three</text>
      <text x="60" y="121">One view of every route.</text>
    </g>
    <g class="t-body" font-size="3.2">
      <text x="172" y="76" font-weight="700">Title Two</text>
      <text x="172" y="81">Alerts when the bus nears.</text>
      <text x="172" y="116" font-weight="700">Title Four</text>
      <text x="172" y="121">Works on any phone browser.</text>
    </g>

    <polygon points="0,170 170,170 174,179 0,179" class="fill-blue"/>
    <polygon points="180,170 238,170 238,179 184,179" class="fill-green"/>
    <text x="5" y="176.5" class="t-foot" font-size="3.4">Harlow-Brenton Holding Co: December 11, 2015</text>
    <text x="175" y="177.5" class="t-body" font-size="5">2</text>
    <text x="189" y="176.5" class="t-foot" font-size="3.4">Proprietary &amp; Confidential</text>
  </svg>
</section>

<!-- Implementation (overview) -->
<section class="slide slide--implementation-a">
  <svg viewBox="0 0 237 181" xmlns="http://www.w3.org/2000/svg">
    <rect x="0" y="6" width="15" height="12" class="fill-blue"/><rect x="17" y="6" width="4" height="12" class="fill-green"/>
    <text x="28" y="16" class="t-head txt-blue" font-size="7.5">Implem<tspan class="txt-green">entation</tspan></text>
    <circle cx="202" cy="10" r="3" class="fill-green"/><text x="207" y="12" class="t-brand" font-size="5">TrakVora</text>

    <rect x="68" y="48" width="104" height="104" class="art" role="img" aria-label="Illustration: a grey head in profile filled with a ring of colourful gear pieces"/>

    <g stroke="var(--orange)" stroke-width="0.5" stroke-dasharray="1 1">
      <line x1="62" y1="65" x2="68" y2="65"/><line x1="62" y1="107" x2="68" y2="107"/>
      <line x1="172" y1="65" x2="182" y2="65"/><line x1="172" y1="107" x2="182" y2="107"/>
    </g>
    <g class="t-muted" font-size="3.2" text-anchor="end">
      <text x="60" y="66">Set up routes and stops.</text>
      <text x="60" y="108">Connect your fleet devices.</text>
    </g>
    <g class="t-muted" font-size="3.2">
      <text x="185" y="66">Train staff in one day.</text>
      <text x="185" y="108">Share the app with families.</text>
    </g>

    <polygon points="0,172 169,172 173,181 0,181" class="fill-blue"/>
    <polygon points="179,172 237,172 237,181 183,181" class="fill-green"/>
    <text x="5" y="178.5" class="t-foot" font-size="3.4">Harlow-Brenton Holding Co: December 11, 2015</text>
    <text x="174" y="179.5" class="t-body" font-size="5">3</text>
    <text x="188" y="178.5" class="t-foot" font-size="3.4">Proprietary &amp; Confidential</text>
  </svg>
</section>

<!-- Implementation (steps) -->
<section class="slide slide--implementation-b">
  <svg viewBox="0 0 234 172" xmlns="http://www.w3.org/2000/svg">
    <rect x="0" y="6" width="15" height="12" class="fill-blue"/><rect x="17" y="6" width="4" height="12" class="fill-green"/>
    <text x="28" y="16" class="t-head txt-blue" font-size="7.5">Implem<tspan class="txt-green">entation</tspan></text>
    <circle cx="199" cy="10" r="3" class="fill-green"/><text x="204" y="12" class="t-brand" font-size="5">TrakVora</text>

    <text x="29" y="32" class="txt-green" font-family="Arimo,sans-serif" font-size="4">A SUBTITLE ABOUT THIS SECTION</text>
    <g class="t-muted" font-size="3.4">
      <text x="29" y="40">Our team works with your transportation office from kickoff to launch, loading</text>
      <text x="29" y="45">routes, stops and vehicles so drivers, parents and directors see the same</text>
      <text x="29" y="50">live data on day one.</text>
    </g>

    <g opacity="0.85">
      <circle cx="62" cy="108" r="33" fill="#4f7fc0"/>
      <circle cx="95" cy="108" r="33" fill="#22a58a"/>
      <circle cx="128" cy="108" r="33" fill="#a8c74a"/>
      <circle cx="161" cy="108" r="33" fill="#e5c43a"/>
      <circle cx="194" cy="108" r="33" fill="#f1c21b"/>
    </g>
    <g class="t-title" font-size="11">
      <text x="41" y="106">1</text><text x="81" y="106">2</text><text x="115" y="106">3</text><text x="148" y="106">4</text><text x="182" y="106">5</text>
    </g>
    <g class="t-num" font-size="3.5" font-weight="400">
      <text x="38" y="116">Plan</text><text x="78" y="116">Load</text><text x="112" y="116">Train</text><text x="145" y="116">Test</text><text x="179" y="116">Launch</text>
    </g>

    <polygon points="0,163 166,163 170,172 0,172" class="fill-blue"/>
    <polygon points="176,163 234,163 234,172 180,172" class="fill-green"/>
    <text x="5" y="169.5" class="t-foot" font-size="3.4">Harlow-Brenton Holding Co: December 11, 2015</text>
    <text x="171" y="170.5" class="t-body" font-size="5">4</text>
    <text x="185" y="169.5" class="t-foot" font-size="3.4">Proprietary &amp; Confidential</text>
  </svg>
</section>

<!-- Pricing (options) -->
<section class="slide slide--pricing-a">
  <svg viewBox="0 0 255 173" xmlns="http://www.w3.org/2000/svg">
    <rect x="0" y="6" width="15" height="12" class="fill-blue"/><rect x="17" y="6" width="4" height="12" class="fill-green"/>
    <text x="31" y="16" class="t-head txt-blue" font-size="7.5">Pri<tspan class="txt-green">cing</tspan></text>
    <circle cx="220" cy="10" r="3" class="fill-green"/><text x="225" y="12" class="t-brand" font-size="5">TrakVora</text>

    <rect x="119" y="48" width="20" height="90" class="art" role="img" aria-label="Illustration: an upright pencil striped in green, orange, red and blue"/>

    <g fill="none" stroke="#aaa" stroke-width="0.5">
      <polyline points="119,62 95,80 50,80"/>
      <polyline points="119,100 95,120 50,120"/>
      <polyline points="139,62 160,66 200,66"/>
      <polyline points="139,105 160,98 200,98"/>
    </g>
    <g fill="var(--white)" stroke="#333" stroke-width="0.6">
      <circle cx="22" cy="44" r="5"/><circle cx="22" cy="83" r="5"/>
      <circle cx="236" cy="48" r="5"/><circle cx="236" cy="87" r="5"/>
    </g>
    <g class="t-body" font-size="4.5" text-anchor="middle">
      <text x="22" y="45.6">1</text><text x="22" y="84.6">2</text><text x="236" y="49.6">3</text><text x="236" y="88.6">4</text>
    </g>
    <g font-family="Arimo,sans-serif" font-size="3.4" font-weight="700" fill="#c0392b">
      <text x="32" y="38">LOREM IPSUM DOLOR</text>
      <text x="32" y="78">LOREM IPSUM DOLOR</text>
      <text x="177" y="38">LOREM IPSUM DOLOR</text>
      <text x="177" y="78">LOREM IPSUM DOLOR</text>
    </g>
    <g class="t-body" font-size="3.2">
      <text x="32" y="43">Cupcake ipsum dolor sit</text><text x="32" y="47">amet pudding wafer.</text><text x="32" y="51">Chocolate bar tiramisu cake</text><text x="32" y="55">topping dessert ice cream</text>
      <text x="32" y="83">Cupcake ipsum dolor sit</text><text x="32" y="87">amet pudding wafer.</text><text x="32" y="91">Chocolate bar tiramisu</text><text x="32" y="95">cake topping dessert ice</text>
      <text x="177" y="43">Cupcake ipsum dolor sit</text><text x="177" y="47">amet pudding wafer.</text><text x="177" y="51">Chocolate bar tiramisu cake</text><text x="177" y="55">topping dessert ice cream</text>
      <text x="177" y="83">Cupcake ipsum dolor sit</text><text x="177" y="87">amet pudding wafer.</text><text x="177" y="91">Chocolate bar tiramisu</text><text x="177" y="95">cake topping dessert ice</text>
    </g>

    <polygon points="0,164 187,164 191,173 0,173" class="fill-blue"/>
    <polygon points="197,164 255,164 255,173 201,173" class="fill-green"/>
    <text x="5" y="170.5" class="t-foot" font-size="3.4">Harlow-Brenton Holding Co: December 11, 2015</text>
    <text x="192" y="171.5" class="t-body" font-size="5">5</text>
    <text x="206" y="170.5" class="t-foot" font-size="3.4">Proprietary &amp; Confidential</text>
  </svg>
</section>

<!-- Pricing (signpost) -->
<section class="slide slide--pricing-b">
  <svg viewBox="0 0 256 181" xmlns="http://www.w3.org/2000/svg">
    <rect x="0" y="6" width="15" height="12" class="fill-blue"/><rect x="17" y="6" width="4" height="12" class="fill-green"/>
    <text x="31" y="17" class="t-head txt-blue" font-size="7.5">Pri<tspan class="txt-green">cing</tspan></text>
    <circle cx="221" cy="10" r="3" class="fill-green"/><text x="226" y="12" class="t-brand" font-size="5">TrakVora</text>

    <circle cx="22" cy="33" r="0.9" fill="#333"/>
    <text x="29" y="34.5" class="t-body" font-size="3.6">Lorem ipsum dolor sit amet consectetur adipiscing elit</text>

    <rect x="86" y="55" width="82" height="90" class="art" role="img" aria-label="Illustration: a wooden signpost with four coloured arrow boards reading Lorem Ipsum, Ipsum Dolor, Site Amet Dolor and Lorem"/>

    <g font-family="Arimo,sans-serif" font-size="3.4" font-weight="700" fill="#a0504e" text-anchor="end">
      <text x="78" y="71">LOREM IPSUM</text><text x="78" y="75">DOLOR</text>
      <text x="78" y="115">LOREM IPSUM</text><text x="78" y="119">DOLOR</text>
    </g>
    <g class="t-body" font-size="3.2" text-anchor="end">
      <text x="78" y="80">Lorem ipsum dolor sit amet,</text><text x="78" y="84">consectetur adipiscing elit, sed do</text><text x="78" y="88">eiusmod tempor incididunt ut</text><text x="78" y="92">labore et dolore magna aliqua.</text>
      <text x="78" y="124">Lorem ipsum dolor sit amet,</text><text x="78" y="128">consectetur adipiscing elit, sed do</text><text x="78" y="132">eiusmod tempor incididunt ut</text><text x="78" y="136">labore et dolore magna aliqua.</text>
    </g>
    <g font-family="Arimo,sans-serif" font-size="3.4" font-weight="700" fill="var(--blue-mid)">
      <text x="175" y="61">LOREM IPSUM</text><text x="175" y="65">DOLOR</text>
    </g>
    <g font-family="Arimo,sans-serif" font-size="3.4" font-weight="700" fill="var(--orange)">
      <text x="175" y="98">LOREM IPSUM</text><text x="175" y="102">DOLOR</text>
    </g>
    <g class="t-body" font-size="3.2">
      <text x="175" y="70">Lorem ipsum dolor sit amet,</text><text x="175" y="74">consectetur adipiscing elit, sed do</text><text x="175" y="78">eiusmod tempor incididunt ut</text><text x="175" y="82">labore et dolore magna aliqua.</text>
      <text x="175" y="107">Lorem ipsum dolor sit amet,</text><text x="175" y="111">consectetur adipiscing elit, sed do</text><text x="175" y="115">eiusmod tempor incididunt ut</text><text x="175" y="119">labore et dolore magna aliqua.</text>
    </g>

    <polygon points="0,172 188,172 192,181 0,181" class="fill-blue"/>
    <polygon points="198,172 256,172 256,181 202,181" class="fill-green"/>
    <text x="5" y="178.5" class="t-foot" font-size="3.4">Harlow-Brenton Holding Co: December 11, 2015</text>
    <text x="193" y="179.5" class="t-body" font-size="5">6</text>
    <text x="207" y="178.5" class="t-foot" font-size="3.4">Proprietary &amp; Confidential</text>
  </svg>
</section>

</body>
</html>
```